Brightwren Farming

We need a logo design for a new company based in Kelowna, BC. We grow market garden vegetables for sale at market and in a CSA program. We try to only use hand tools for all aspects of cultivating, seeding, weeding, harvesting and distributing. For this reason we consider ourselves very low impact on the environment.

We would like blues and green in the design with an earthy, natural feel

Target Market(s)

Environmentally aware, health conscience

Industry/Entity Type

Farming

Requirements
Must have
• Foot prints with section for contact details all on the one side
Should not have
• Dark, black colours or anything that looks unnatural

```html
<!DOCTYPE html>
<html lang="en">
<head>
<meta charset="utf-8">
<title>Brightwren Farming – Business Card</title>
<link href="https://fonts.googleapis.com/css2?family=Lato:wght@400;700;900&display=swap" rel="stylesheet">
<style>
  :root {
    --page-bg: #e4e4e2;
    --card-green: #466b34;
    --card-ink: #ffffff;
    --card-ink-soft: rgba(255,255,255,0.9);
  }
  html, body {
    margin: 0;
    padding: 0;
    width: 1200px;
    height: 800px;
    overflow: hidden;
    background: var(--page-bg);
    font-family: "Lato", Arial, sans-serif;
  }
  .canvas {
    position: relative;
    width: 1200px;
    height: 800px;
  }
  .card {
    position: absolute;
    left: 75px;
    top: 100px;
    width: 1050px;
    height: 600px;
    background: var(--card-green);
    color: var(--card-ink);
    box-shadow: 0 6px 18px rgba(0,0,0,0.18);
  }
  .identity {
    position: absolute;
    left: 95px;
    top: 205px;
  }
  .identity__name {
    margin: 0;
    font-weight: 900;
    font-size: 32px;
    letter-spacing: 1px;
    text-transform: uppercase;
    line-height: 1.1;
  }
  .identity__role {
    margin: 4px 0 0 24px;
    font-weight: 400;
    font-size: 17px;
    letter-spacing: 0.5px;
    text-transform: uppercase;
    color: var(--card-ink-soft);
  }
  .brand {
    position: absolute;
    left: 215px;
    top: 330px;
    width: 230px;
    height: 230px;
    box-sizing: border-box;
    border: 4px solid var(--card-ink);
    display: flex;
    align-items: center;
    justify-content: center;
    text-align: center;
  }
  .brand__name {
    font-weight: 700;
    font-size: 24px;
    line-height: 1.25;
    letter-spacing: 1px;
    text-transform: uppercase;
    color: var(--card-ink);
  }
  .contact {
    position: absolute;
    left: 720px;
    top: 190px;
    margin: 0;
    padding: 0;
    list-style: none;
  }
  .contact__item {
    display: flex;
    align-items: center;
    gap: 12px;
    margin-bottom: 12px;
    font-size: 15px;
    color: var(--card-ink-soft);
  }
  .contact__icon {
    width: 20px;
    height: 20px;
    flex: none;
  }
</style>
</head>
<body>
<div class="canvas">
  <section class="card" aria-label="Brightwren Farming business card">
    <div class="identity">
      <h1 class="identity__name">Dana Whitfield</h1>
      <p class="identity__role">Art Director</p>
    </div>

    <div class="brand">
      <span class="brand__name">Brightwren<br>Farming</span>
    </div>

    <ul class="contact">
      <li class="contact__item">
        <svg class="contact__icon" viewBox="0 0 22 22" aria-hidden="true">
          <circle cx="11" cy="11" r="9.5" fill="none" stroke="#fff" stroke-width="1.3"/>
          <text x="11" y="15" text-anchor="middle" font-family="Lato, sans-serif" font-size="11" fill="#fff">P</text>
        </svg>
        <span>(250) 555-0147</span>
      </li>
      <li class="contact__item">
        <svg class="contact__icon" viewBox="0 0 22 22" aria-hidden="true">
          <circle cx="11" cy="11" r="9.5" fill="none" stroke="#fff" stroke-width="1.3"/>
          <text x="11" y="15" text-anchor="middle" font-family="Lato, sans-serif" font-size="11" fill="#fff">E</text>
        </svg>
        <span>hello@brightwrenfarm.ca</span>
      </li>
      <li class="contact__item">
        <svg class="contact__icon" viewBox="0 0 22 22" aria-hidden="true">
          <circle cx="11" cy="11" r="9.5" fill="none" stroke="#fff" stroke-width="1.3"/>
          <text x="11" y="15" text-anchor="middle" font-family="Lato, sans-serif" font-size="10" fill="#fff">W</text>
        </svg>
        <span>www.brightwrenfarm.ca</span>
      </li>
    </ul>
  </section>
</div>
</body>
</html>
```